Business Card Design Project

Business card design for an IT Service company. A logo has already been created in a different contest and has been attached to this project. Ideally we're looking for a double sided business card that matches the look and feel of our newly created logo.

We're open to creativity if you feel a tag line is needed such as "IT Services and Application Development". We're open to really and look and feel - even single sided business cards if you feel you have something that's a great idea.

Last thought here - I'm not sure how it'll look but maybe a two tone card? One side dark blue and the other side white? Don't limit the design submissions to this tho - just curious if it would look good

Nothing too busy please - simple... Thank you and happy designing!

Target Market(s)

Businesses that require IT Services and support for hosted services, technical consultation, web design.

Industry/Entity Type

Business

Font styles to use
Sans Serif

Requirements
Must have
• Use the colors provided in the logo (see attachment) or additional colors that compliment
Must have the following contact info (not necessarily in this order):
- Alan Fisk
- Founding Partner
- afisk@quillbarrow.example
- 555-382-1946
- www.quillbarrow.example

```html
<!DOCTYPE html>
<html lang="en">
<head>
<meta charset="utf-8">
<title>Quillbarrow Business Card</title>
<link href="https://fonts.googleapis.com/css2?family=Arimo:wght@400;700&display=swap" rel="stylesheet">
<style>
  :root {
    --navy: #0b1a42;
    --green: #6cc23a;
    --green-text: #5aa532;
    --white: #ffffff;
    --backdrop: #e4e6ea;
    --edge: #d3d6dc;
  }
  * { box-sizing: border-box; margin: 0; padding: 0; }
  html, body {
    width: 1200px; height: 960px; overflow: hidden;
    background: var(--backdrop);
    font-family: "Arimo", Arial, sans-serif;
  }
  .sheet {
    position: relative; width: 1200px; height: 960px;
    display: flex; flex-direction: column; align-items: center; justify-content: center; gap: 48px;
  }
  .card {
    position: relative; width: 700px; height: 400px;
    background: var(--white);
    box-shadow: 0 6px 18px rgba(0,0,0,0.14);
    overflow: hidden;
  }
  /* Brand lockup */
  .brand { display: flex; align-items: center; gap: 14px; }
  .brand-mark { width: 34px; height: 34px; background: var(--green); flex: none; }
  .brand-name { font-weight: 700; color: var(--navy); font-size: 50px; letter-spacing: -0.5px; line-height: 1; }

  /* Front */
  .card-front { display: flex; flex-direction: column; align-items: center; justify-content: center; }
  .card-front .tagline {
    margin-top: 14px; color: var(--green-text); font-size: 22px; letter-spacing: 0.2px;
  }

  /* Back */
  .card-back .top {
    position: absolute; left: 0; top: 0; width: 100%; height: 168px;
    display: flex; align-items: center; justify-content: center; padding-left: 120px;
  }
  .card-back .stripe { position: absolute; left: 0; top: 168px; width: 100%; height: 16px; background: var(--green); }
  .card-back .panel { position: absolute; left: 0; top: 184px; width: 100%; bottom: 0; background: var(--navy); padding: 30px 44px; }
  .person-name { color: var(--white); font-weight: 700; font-size: 40px; line-height: 1; }
  .person-title { color: var(--green); font-size: 20px; margin-top: 6px; }
  .contact-list { list-style: none; margin-top: 22px; display: flex; flex-direction: column; gap: 12px; }
  .contact-item { display: flex; align-items: center; gap: 16px; color: var(--white); font-size: 20px; }
  .contact-icon { width: 20px; height: 20px; flex: none; }
</style>
</head>
<body>
<main class="sheet">
  <section class="card card-front" aria-label="Card front">
    <div class="brand">
      <span class="brand-mark"></span>
      <span class="brand-name">Quillbarrow</span>
    </div>
    <p class="tagline">IT Services and Application Development</p>
  </section>

  <section class="card card-back" aria-label="Card back">
    <div class="top">
      <div class="brand">
        <span class="brand-mark"></span>
        <span class="brand-name">Quillbarrow</span>
      </div>
    </div>
    <div class="stripe"></div>
    <div class="panel">
      <h1 class="person-name">Alan Fisk</h1>
      <p class="person-title">Founding Partner</p>
      <ul class="contact-list">
        <li class="contact-item">
          <svg class="contact-icon" viewBox="0 0 24 24" aria-hidden="true"><path fill="#6cc23a" d="M6.6 10.8a15.1 15.1 0 0 0 6.6 6.6l2.2-2.2a1 1 0 0 1 1-.25 11.4 11.4 0 0 0 3.6.57 1 1 0 0 1 1 1V20a1 1 0 0 1-1 1A17 17 0 0 1 3 4a1 1 0 0 1 1-1h3.5a1 1 0 0 1 1 1c0 1.25.2 2.46.57 3.6a1 1 0 0 1-.25 1z"/></svg>
          <span>555-382-1946</span>
        </li>
        <li class="contact-item">
          <svg class="contact-icon" viewBox="0 0 24 24" aria-hidden="true"><rect x="2" y="5" width="20" height="14" fill="#6cc23a"/><path d="M2 5l10 8 10-8" fill="none" stroke="#0b1a42" stroke-width="1.6"/></svg>
          <span>afisk@quillbarrow.example</span>
        </li>
        <li class="contact-item">
          <svg class="contact-icon" viewBox="0 0 24 24" aria-hidden="true"><circle cx="12" cy="12" r="10" fill="#6cc23a"/><g fill="none" stroke="#0b1a42" stroke-width="1.4"><ellipse cx="12" cy="12" rx="4.5" ry="10"/><path d="M2 12h20M4 7h16M4 17h16"/></g></svg>
          <span>www.quillbarrow.example</span>
        </li>
      </ul>
    </div>
  </section>
</main>
</body>
</html>
```